Larchmere Hockey Academy

We are are Ice Hockey Development Company that provided on-ice Hockey development services. We need a Landing Page with tabs to direct to individual program pages.
Landing Page
About Page
Winter Program Page
Spring Program Page
Summer Program Page
Team Page
Tournament Page

```html
<!DOCTYPE html>
<html lang="en">
<head>
<meta charset="utf-8">
<title>Larchmere Hockey Academy</title>
<link href="https://fonts.googleapis.com/css2?family=Roboto:wght@400;500;700;900&display=swap" rel="stylesheet">
<style>
:root{
  --black:#050505;
  --ink:#111;
  --green-dark:#0b6e0b;
  --green:#17a017;
  --grey-bg:#f3f3f3;
  --card-grey:#f4f4f4;
  --white:#fff;
  --muted:#333;
}
*{margin:0;padding:0;box-sizing:border-box}
html,body{width:1200px;height:3987px;overflow:hidden}
body{position:relative;font-family:'Roboto',sans-serif;color:var(--ink);background:var(--white)}
.abs{position:absolute}
.photo{position:absolute;overflow:hidden}
.site-header{position:absolute;left:0;top:0;width:1200px;height:90px;background:var(--black)}
.brand{position:absolute;left:111px;top:18px;color:var(--white);font-weight:900;font-size:19px;line-height:19px;letter-spacing:1px;display:flex;align-items:center;gap:8px}
.brand .mark{width:12px;height:12px;background:var(--white)}
.main-nav{position:absolute;left:299px;top:36px;display:flex;gap:0}
.main-nav a{position:absolute;color:var(--white);font-size:14px;font-weight:700;letter-spacing:.6px;text-decoration:none;white-space:nowrap}
.main-nav a.active{border-bottom:2px solid var(--white);padding-bottom:2px}
.search{position:absolute;left:1059px;top:32px}
.hero{position:absolute;left:0;top:90px;width:1200px;height:550px;background-color:var(--grey-bg);
  background-image:radial-gradient(#d6d6d6 1px,transparent 1.5px);background-size:14px 14px;overflow:hidden}
.hero-watermark{position:absolute;left:170px;top:35px;font-weight:900;font-size:210px;line-height:190px;color:#fff;letter-spacing:4px}
.hero h1{position:absolute;left:111px;top:140px;font-size:57px;line-height:57px;font-weight:700;color:var(--black)}
.btn{display:inline-flex;align-items:center;justify-content:center;font-weight:500;text-decoration:none}
.btn-solid{background:var(--green-dark);color:var(--white)}
.btn-outline{border:1px solid var(--green-dark);color:var(--ink);background:var(--white)}
.hero .btn{position:absolute;top:348px;width:182px;height:54px;font-size:18px}
.highlights{position:absolute;top:640px;left:0;width:1200px;height:306px}
.fair-play{position:absolute;left:402px;top:0;width:403px;height:306px;background:var(--green-dark);color:var(--white);text-align:center}
.fair-play .num{position:absolute;top:52px;width:100%;font-size:58px;font-weight:700;color:rgba(255,255,255,.12)}
.fair-play h3{position:absolute;top:128px;width:100%;font-size:35px;font-weight:700}
.fair-play p{position:absolute;top:180px;left:120px;width:163px;font-size:11px;line-height:15px}
.games{position:absolute;top:946px;left:0;width:1200px;height:290px;background:var(--white);text-align:center;overflow:hidden}
.games .dots{position:absolute;left:220px;top:70px;width:760px;height:200px;background-image:radial-gradient(#d6d6d6 1px,transparent 1.5px);background-size:16px 16px}
.games .wm{position:absolute;left:0;width:100%;top:30px;font-size:240px;line-height:240px;font-weight:900;color:#f1f1f1;letter-spacing:4px}
.games .eyebrow{position:absolute;top:104px;width:100%;font-size:14px;font-weight:500}
.games h2{position:absolute;top:124px;width:100%;font-size:45px;font-weight:700}
.section-title{position:absolute;width:100%;text-align:center;font-size:37px;font-weight:700;color:var(--black)}
.news{position:absolute;top:1236px;left:0;width:1200px;height:905px;background:var(--grey-bg)}
.news-card{position:absolute;top:105px;height:390px}
.news-card .cap{position:absolute;top:305px;left:0;right:0;height:85px;background:var(--green-dark);color:var(--white);font-size:12.5px;line-height:15px;padding:20px 20px 0}
.about{position:absolute;top:1718px;left:0;width:1200px;height:423px;background:var(--white)}
.about .frame{position:absolute;left:124px;top:47px;width:461px;height:322px;background:var(--green-dark)}
.about h2{position:absolute;left:638px;top:116px;font-size:30px;font-weight:700}
.about p{position:absolute;left:638px;top:174px;width:370px;font-size:14.5px;line-height:19px;color:var(--muted)}
.about .btn{position:absolute;left:638px;top:282px;width:181px;height:54px;font-size:18px}
.tournament{position:absolute;left:0;width:1200px}
.cards{position:absolute;left:111px;width:975px;display:flex;justify-content:space-between}
.card{width:307px;height:382px;background:var(--white);position:relative}
.tournament.alt .card{background:var(--card-grey)}
.card .photo{left:0;top:0;width:307px;height:164px}
.card .label{position:absolute;top:164px;width:100%;height:68px;background:var(--green);color:var(--white);font-weight:700;font-size:17.5px;line-height:18px;text-align:center;display:flex;align-items:center;justify-content:center}
.card .meta{position:absolute;top:255px;width:100%;text-align:center;font-size:15px}
.card .meta span{display:inline-block;margin:0 12px}
.card .sep{display:inline-block;width:1px;height:17px;background:#333;vertical-align:middle}
.card .fee{position:absolute;top:290px;width:100%;text-align:center;font-size:10.5px}
.card .btn{position:absolute;top:319px;left:77px;width:153px;height:46px;background:var(--green-dark);color:var(--white);font-size:15px}
.site-footer{position:absolute;top:3737px;left:0;width:1200px;height:250px;background:var(--black);color:var(--white)}
.site-footer .brand{top:42px;font-size:26px;line-height:26px}
.copy{position:absolute;left:111px;top:133px;font-size:14px}
.foot-links{position:absolute;left:390px;top:43px;list-style:none;font-size:14px;line-height:22.5px}
.social{position:absolute;left:576px;top:46px;list-style:none}
.social li{display:flex;align-items:center;gap:14px;height:43px;font-size:18px}
.social .dot{width:34px;height:34px;border:2px solid var(--white);border-radius:50%}
.newsletter{position:absolute;left:796px;top:46px}
.newsletter h4{font-size:22px;font-weight:500}
.newsletter form{display:flex;margin-top:12px}
.newsletter .field{width:187px;height:31px;border:1px solid #777;color:#ccc;font-size:10px;padding-left:14px;display:flex;align-items:center}
.newsletter .go{width:104px;height:31px;background:var(--white);color:var(--ink);font-size:11px;display:flex;align-items:center;justify-content:center}
</style>
</head>
<body>

<header class="site-header">
  <div class="brand"><span>LARCHMERE<br>HOCKEY</span></div>
  <nav class="main-nav">
    <a class="active" style="left:0">HOME</a>
    <a style="left:68px">NEWS</a>
    <a style="left:139px">EVENTS</a>
    <a style="left:224px">GALLERY</a>
    <a style="left:320px">ABOUT US</a>
    <a style="left:430px">BLOG</a>
  </nav>
  <svg class="search" width="28" height="28" viewBox="0 0 28 28"><circle cx="12" cy="12" r="10" fill="none" stroke="#fff" stroke-width="2"/><line x1="19" y1="19" x2="27" y2="27" stroke="#fff" stroke-width="2"/></svg>
</header>

<section class="hero">
  <div class="hero-watermark">ICE<br>HOCKEY</div>
  <h1>WELCOME TO<br>LARCHMERE HOCKEY<br>ACADEMY</h1>
  <a class="btn btn-solid" style="left:111px">Read More</a>
  <a class="btn btn-outline" style="left:314px">Contact Us</a>
  <div class="photo" role="img" aria-label="Two hockey players facing off with sticks" style="left:573px;top:111px;width:518px;height:434px;background:radial-gradient(ellipse at 35% 50%,#c9a23a 0,#7c7c7c 25%,rgba(243,243,243,0) 55%),radial-gradient(ellipse at 72% 45%,#2a3f9a 0,rgba(243,243,243,0) 45%)"></div>
</section>

<section class="highlights">
  <div class="photo" role="img" aria-label="Young player in red skating on ice rink" style="left:0;top:0;width:402px;height:306px;background:linear-gradient(160deg,#6d4a3c,#c9443f 40%,#d9dde3 75%,#b8c2cc)"></div>
  <div class="fair-play">
    <div class="num">02</div>
    <h3>FAIR PLAY</h3>
    <p>Etiam ultricies nisi vel augue, nulla ut me varius laoreet. Phasellus viverra nulla ut metus varius laoreet</p>
  </div>
  <div class="photo" role="img" aria-label="Player in team jersey raising his stick under arena lights" style="left:805px;top:0;width:395px;height:306px;background:radial-gradient(circle at 60% 55%,#e6e2d4 0,#3a5a88 40%,#0d1d3a 80%)"></div>
</section>

<section class="games">
  <div class="dots"></div>
  <div class="wm">GAMES</div>
  <div class="eyebrow">WHAT'S TRENDING</div>
  <h2>UPCOMING GAMES 2021.</h2>
</section>

<section class="news">
  <h2 class="section-title" style="top:36px">RECENT NEWS</h2>
  <article class="news-card" style="left:0;width:288px">
    <div class="photo" role="img" aria-label="Coach talking to young players on the ice" style="left:0;top:0;width:288px;height:305px;background:linear-gradient(180deg,#2f4258,#4a4f55 55%,#c9a126)"></div>
    <div class="cap">WHC President Daniel Orsay met GSC President Henrik Vale today at the.</div>
  </article>
  <article class="news-card" style="left:291px;width:317px">
    <div class="photo" role="img" aria-label="Two players battling for the puck" style="left:0;top:0;width:317px;height:305px;background:linear-gradient(120deg,#d9dde2,#5a4a4e 45%,#2a2226 70%,#bfc7cf)"></div>
    <div class="cap">The Continental Hockey Union (CHU) elected its new executive board in its Ordinary.</div>
  </article>
  <article class="news-card" style="left:611px;width:318px">
    <div class="photo" role="img" aria-label="Player in white and red skating with the puck" style="left:0;top:0;width:318px;height:305px;background:linear-gradient(170deg,#cfd5da,#e9e4da 45%,#5a3a2c 70%,#c9cfd6)"></div>
    <div class="cap">The Continental Hockey Union held its Executive Board Meeting at the Pinecrest Resort Harbin Bay.</div>
  </article>
  <article class="news-card" style="left:932px;width:268px">
    <div class="photo" role="img" aria-label="Player skating outdoors at sunset" style="left:0;top:0;width:268px;height:305px;background:linear-gradient(180deg,#e8b27a,#9fa6b0 40%,#3c4a5a 65%,#c9d2da)"></div>
    <div class="cap">The Continental Hockey Union (CHU) is set to host its biggest meeting 2023.</div>
  </article>
</section>

<section class="about">
  <div class="frame"></div>
  <div class="photo" role="img" aria-label="Goalkeeper defending the net between players" style="left:111px;top:56px;width:462px;height:322px;background:linear-gradient(180deg,#1c2a4a,#b2343a 45%,#dfe3e8 80%)"></div>
  <h2>ABOUT US</h2>
  <p>Vel illum dolore eu feugiat nulla facilisis at vero eros et accu qui blandit praesent luptatum zzril delenit augue dolore eu. Autem vel eum iriure dolor in hendrerit in vulputate veli.</p>
  <a class="btn btn-solid">Read More</a>
</section>

<section class="tournament" style="top:2141px;height:522px;background:var(--grey-bg)">
  <h2 class="section-title" style="top:28px">WINTER TOURNAMENT</h2>
  <div class="cards" style="top:99px">
    <div class="card"><div class="photo" role="img" aria-label="Player skating in an arena" style="background:linear-gradient(180deg,#1a2a55,#7a8aa8 50%,#e1e5ea)"></div><div class="label">58th Kestrel Senior<br>Hockey Tournament (Men)</div><div class="meta"><span>12 January</span><i class="sep"></i><span>Secunderabad</span></div><div class="fee">Enter Fee Per Team $560 &nbsp;|&nbsp; 20 Team Limit</div><a class="btn">Register Now</a></div>
    <div class="card"><div class="photo" role="img" aria-label="Players in front of the goal" style="background:linear-gradient(180deg,#1a2a55,#6b7896 50%,#dfe3e8)"></div><div class="label">Weekend Hockey<br>Tournament 2023</div><div class="meta"><span>6-4 November</span><i class="sep"></i><span>Meridian Stadium</span></div><div class="fee">Enter Fee Per Team $600 &nbsp;|&nbsp; 20 Team Limit</div><a class="btn">Register Now</a></div>
    <div class="card"><div class="photo" role="img" aria-label="Player shooting at an empty net" style="background:linear-gradient(180deg,#22305a,#7c889e 50%,#e3e6ea)"></div><div class="label">Memorial Hockey<br>Tournament 2022</div><div class="meta"><span>6-7 March</span><i class="sep"></i><span>Jalandhar</span></div><div class="fee">Enter Fee Per Team $650 &nbsp;|&nbsp; 20 Team Limit</div><a class="btn">Register Now</a></div>
  </div>
</section>

<section class="tournament alt" style="top:2663px;height:538px;background:var(--white)">
  <h2 class="section-title" style="top:30px">SPRING TOURNAMENT</h2>
  <div class="cards" style="top:110px">
    <div class="card"><div class="photo" role="img" aria-label="Players skating in a dark arena" style="background:linear-gradient(180deg,#0e1a36,#4d5a78 55%,#cdd4dc)"></div><div class="label">Tribal Women Hockey<br>Tournament 2023</div><div class="meta"><span>11 February</span><i class="sep"></i><span>Meridian Stadium</span></div><div class="fee">Enter Fee Per Team $580 &nbsp;|&nbsp; 20 Team Limit</div><a class="btn">Register Now</a></div>
    <div class="card"><div class="photo" role="img" aria-label="Player in blue jersey skating forward" style="background:linear-gradient(180deg,#142244,#2f4ea0 50%,#cfd6de)"></div><div class="label">National Youth Games<br>2022 (Women)</div><div class="meta"><span>10 February</span><i class="sep"></i><span>Gwalior</span></div><div class="fee">Enter Fee Per Team $500 &nbsp;|&nbsp; 20 Team Limit</div><a class="btn">Register Now</a></div>
    <div class="card"><div class="photo" role="img" aria-label="Close view of sticks and puck on ice" style="background:linear-gradient(180deg,#e9ecef,#c8cdd3 50%,#e8c9cc)"></div><div class="label">Inter-Department National<br>Championship 2023</div><div class="meta"><span>13 March</span><i class="sep"></i><span>Bengaluru</span></div><div class="fee">Enter Fee Per Team $400 &nbsp;|&nbsp; 20 Team Limit</div><a class="btn">Register Now</a></div>
  </div>
</section>

<section class="tournament" style="top:3201px;height:536px;background:var(--grey-bg)">
  <h2 class="section-title" style="top:44px">SUMMER TOURNAMENT</h2>
  <div class="cards" style="top:110px">
    <div class="card"><div class="photo" role="img" aria-label="Goalkeeper diving in front of the net" style="background:linear-gradient(180deg,#1a2448,#b53438 50%,#e0e4e8)"></div><div class="label">Men's Hockey<br>Tournament 2023</div><div class="meta"><span>10 Aprile</span><i class="sep"></i><span>Meridian Stadium</span></div><div class="fee">Enter Fee Per Team $580 &nbsp;&nbsp; 20 Team Limit</div><a class="btn">Register Now</a></div>
    <div class="card"><div class="photo" role="img" aria-label="Player in dark jersey with stick raised" style="background:linear-gradient(180deg,#3a4f86,#1e1e24 50%,#9a2f34)"></div><div class="label">Women's Hockey<br>Tournament 2023</div><div class="meta"><span>13 Aprile</span><i class="sep"></i><span>Lucknow</span></div><div class="fee">Enter Fee Per Team $580 &nbsp;&nbsp; 20 Team Limit</div><a class="btn">Register Now</a></div>
    <div class="card"><div class="photo" role="img" aria-label="Two players chasing the puck" style="background:linear-gradient(180deg,#2a3550,#7c8594 50%,#d3d8dd)"></div><div class="label">Invitational Prize Money<br>Hockey Tournament</div><div class="meta"><span>15 Aprile</span><i class="sep"></i><span>Jharkhand</span></div><div class="fee">Enter Fee Per Team $580 &nbsp;&nbsp; 20 Team Limit</div><a class="btn">Register Now</a></div>
  </div>
</section>

<footer class="site-footer">
  <div class="brand"><span>LARCHMERE<br>HOCKEY</span></div>
  <div class="copy">© Larchmere Hockey Development</div>
  <ul class="foot-links">
    <li>Home</li><li>News</li><li>Events</li><li>Media Gallery</li><li>Development</li><li>Resoures</li><li>About</li><li>Contact Us</li>
  </ul>
  <ul class="social">
    <li><span class="dot"></span>Friendlink</li>
    <li><span class="dot"></span>Chirper</li>
    <li><span class="dot"></span>Snapgram</li>
    <li><span class="dot"></span>Viewtube</li>
  </ul>
  <div class="newsletter">
    <h4>Subscribe To Our Newsletter</h4>
    <form><div class="field">Enter your email</div><div class="go">Subscribe</div></form>
  </div>
</footer>

</body>
</html>
```